Business Cards

Need a neat design for a new business card

Industry/Entity Type

Residential Construction

Contact Information for Business Card

Company Name- KORV Construction Inc.
Owner- Daniel Pruitt
Phone number- (555)270-4418
Email- korvcobuilds@mailbox-example.com
Facebook- www.socialpage-example.com/korvcobuilds

Colors
fefdec

```html
<!DOCTYPE html>
<html lang="en">
<head>
<meta charset="UTF-8">
<title>KORV Construction Inc. – Business Card</title>
<link rel="stylesheet" href="https://fonts.googleapis.com/css2?family=Marcellus&family=Montserrat:wght@400;500&display=swap">
<style>
  :root {
    --stage: #2a2a2a;
    --card-dark: #0b0b0b;
    --card-light: #fefefe;
    --ink: #161616;
    --silver: #c9c9c9;
    --rule: #3a3a3a;
  }
  * { box-sizing: border-box; margin: 0; padding: 0; }
  html, body {
    width: 1200px;
    height: 900px;
    overflow: hidden;
  }
  body {
    background: var(--stage);
    display: flex;
    flex-direction: column;
    align-items: center;
    justify-content: center;
    gap: 36px;
  }
  .card {
    width: 700px;
    height: 400px;
    box-shadow: 0 10px 30px rgba(0,0,0,0.45);
    position: relative;
  }
  .card-front {
    background: var(--card-dark);
    display: flex;
    align-items: center;
    justify-content: center;
  }
  .front-brand {
    font-family: "Marcellus", serif;
    font-size: 44px;
    letter-spacing: 4px;
    color: var(--silver);
  }
  .card-back {
    background: var(--card-light);
    display: flex;
    align-items: center;
    padding: 0 40px 0 48px;
  }
  .brand-frame {
    width: 300px;
    height: 150px;
    border: 2px solid var(--ink);
    display: flex;
    align-items: center;
    justify-content: center;
    flex-shrink: 0;
  }
  .brand-name {
    font-family: "Marcellus", serif;
    font-size: 26px;
    letter-spacing: 1px;
    color: var(--ink);
    text-align: center;
    line-height: 1.25;
  }
  .details {
    margin-left: 26px;
    display: flex;
    flex-direction: column;
    gap: 18px;
  }
  .owner-block, .contact-block {
    border-left: 1.5px solid var(--rule);
    padding-left: 18px;
  }
  .owner-name {
    font-family: "Marcellus", serif;
    font-size: 26px;
    color: var(--ink);
    letter-spacing: 1px;
    text-transform: uppercase;
  }
  .owner-role {
    font-family: "Marcellus", serif;
    font-size: 14px;
    color: var(--ink);
    text-transform: uppercase;
    letter-spacing: 1px;
  }
  .contact-list { list-style: none; }
  .contact-item {
    display: flex;
    align-items: center;
    gap: 10px;
    font-family: "Montserrat", sans-serif;
    font-size: 14px;
    color: var(--ink);
    line-height: 1.75;
    white-space: nowrap;
  }
  .contact-icon { width: 14px; height: 14px; flex-shrink: 0; }
</style>
</head>
<body>
  <section class="card card-front">
    <div class="front-brand">KORV Construction Inc.</div>
  </section>

  <section class="card card-back">
    <div class="brand-frame">
      <div class="brand-name">KORV<br>Construction Inc.</div>
    </div>
    <div class="details">
      <div class="owner-block">
        <div class="owner-name">Daniel Pruitt</div>
        <div class="owner-role">Owner</div>
      </div>
      <div class="contact-block">
        <ul class="contact-list">
          <li class="contact-item">
            <svg class="contact-icon" viewBox="0 0 16 16" aria-hidden="true">
              <circle cx="8" cy="8" r="7" fill="none" stroke="#161616" stroke-width="1.3"/>
              <path d="M5.5 4.8l1.3-.3.8 1.7-.8.6a4.5 4.5 0 0 0 2 2l.6-.8 1.7.8-.3 1.3c-3 .2-5.5-2.3-5.3-5.3z" fill="#161616"/>
            </svg>
            (555) 270-4418
          </li>
          <li class="contact-item">
            <svg class="contact-icon" viewBox="0 0 16 16" aria-hidden="true">
              <rect x="1" y="3.5" width="14" height="9" fill="none" stroke="#161616" stroke-width="1.3"/>
              <path d="M1 3.5l7 5 7-5" fill="none" stroke="#161616" stroke-width="1.3"/>
            </svg>
            korvcobuilds@mailbox-example.com
          </li>
          <li class="contact-item">
            <svg class="contact-icon" viewBox="0 0 16 16" aria-hidden="true">
              <circle cx="8" cy="8" r="7" fill="#161616"/>
            </svg>
            socialpage-example.com/korvcobuilds
          </li>
        </ul>
      </div>
    </div>
  </section>
</body>
</html>
```